Bussiness Card Vanta Cargo

I need a bussiness cards design, for a logistics company named Vanta Cargo. Logo is attached.
The information needed is:
- Name
- Job Title
- Email
- Celphone
- Website

```html
<!DOCTYPE html>
<html lang="en">
<head>
<meta charset="utf-8">
<title>Vanta Cargo – Business Cards</title>
<link href="https://fonts.googleapis.com/css2?family=Montserrat:wght@600;700&family=Roboto:wght@400;500;700&display=swap" rel="stylesheet">
<style>
  :root{
    --page:#2b2b2d;
    --card:#262627;
    --red:#e3262b;
    --white:#ffffff;
    --muted:#d9d9d9;
  }
  *{margin:0;padding:0;box-sizing:border-box}
  html,body{width:1200px;height:885px;overflow:hidden}
  body{background:var(--page);position:relative;font-family:"Roboto",Arial,sans-serif}
  .card{position:absolute;width:540px;height:310px;background:var(--card);border-radius:22px;box-shadow:0 10px 30px rgba(0,0,0,.35);overflow:hidden}
  .card--front{left:90px;top:120px}
  .card--back{left:570px;top:455px}

  .brand{display:flex;align-items:center;gap:12px}
  .brand__mark{width:26px;height:26px;background:var(--red)}
  .brand__name{font-family:"Montserrat",Arial,sans-serif;font-weight:700;color:var(--white);letter-spacing:.5px;text-transform:uppercase}

  .card--front .brand{position:absolute;left:0;right:0;top:112px;justify-content:center}
  .card--front .brand__mark{width:34px;height:34px}
  .card--front .brand__name{font-size:40px}
  .front__web{position:absolute;left:0;right:0;top:228px;text-align:center;color:var(--muted);font-size:14px;letter-spacing:1.2px}
  .front__web span{color:var(--red)}

  .card--back .brand{position:absolute;right:44px;top:54px}
  .card--back .brand__name{font-size:26px}
  .back__rule{position:absolute;right:40px;top:112px;width:290px;height:1.5px;background:var(--red)}

  .person{position:absolute;left:44px;top:178px}
  .person__bar{position:absolute;left:0;top:182px;width:5px;height:36px;background:var(--red)}
  .person__name{font-weight:700;font-size:20px;color:var(--red);line-height:1}
  .person__name-rule{position:absolute;left:175px;top:10px;width:120px;height:1px;background:var(--red)}
  .person__title{font-size:14px;color:var(--white);margin-top:4px}

  .contacts{position:absolute;left:44px;top:232px;list-style:none}
  .contacts li{display:flex;align-items:center;gap:8px;color:var(--white);font-size:13px;line-height:20px}
  .contacts svg{width:12px;height:12px;fill:var(--red)}
</style>
</head>
<body>

<section class="card card--front">
  <div class="brand">
    <span class="brand__mark"></span>
    <span class="brand__name">Vanta Cargo</span>
  </div>
  <p class="front__web">www.<span>vantacargo</span>.ca</p>
</section>

<section class="card card--back">
  <div class="brand">
    <span class="brand__mark"></span>
    <span class="brand__name">Vanta Cargo</span>
  </div>
  <div class="back__rule"></div>

  <div class="person__bar"></div>
  <div class="person">
    <p class="person__name">Dorian Velescu</p>
    <span class="person__name-rule"></span>
    <p class="person__title">President</p>
  </div>

  <ul class="contacts">
    <li>
      <svg viewBox="0 0 24 24" aria-hidden="true"><path d="M6.6 10.8a15.1 15.1 0 0 0 6.6 6.6l2.2-2.2a1 1 0 0 1 1-.25 11.4 11.4 0 0 0 3.6.57 1 1 0 0 1 1 1V20a1 1 0 0 1-1 1A17 17 0 0 1 3 4a1 1 0 0 1 1-1h3.5a1 1 0 0 1 1 1c0 1.25.2 2.45.57 3.57a1 1 0 0 1-.25 1z"/></svg>
      (555) 014-2270
    </li>
    <li>
      <svg viewBox="0 0 24 24" aria-hidden="true"><path d="M2 5h20v14H2z M2 5l10 8 10-8" /></svg>
      dorian@vantacargo.ca
    </li>
    <li>
      <svg viewBox="0 0 24 24" aria-hidden="true"><circle cx="12" cy="12" r="10"/></svg>
      www.vantacargo.ca
    </li>
  </ul>
</section>

</body>
</html>
```